Bayside Critter Welcome MEET

Hi ALL!
We need an 8.5 X 11 inch, one page flyer to include all the below copy plus 8 sponsoring logos at the very bottom.
Thank YOU!

Birch Hollow Critter MEET
(Fun for Animals In Rescue!)

Sunday, August 12, 2018
1 to 4:30 p.m.

Animal Education & Adoption Event
featuring:

Harbor Pet Shelter & Services Rabbits & Mice

Meadow Browsers Goats

Kindly Hounds Haven

Featherwing Pigeons & Doves

Comet Pup Haven

Marge’s Feline Haven

Marvel Mutt Haven

Special Guest from 1-3 p.m.
BeBop - SF's 1st Therapy Pig!
Instagram: @BEBOP_BAYHOG
Facebook: @BEBOP THE HOG

Activities for Kids
Dog & Cat Toy Making with Greta Holloway Canine School
Animal Mask Making with Tiny Crafters
Face-in-a-Hole Photo Fun with Mark Dorsey Canine School

HPSS FREE Giveaway!
First 75 attending families receive a FREE PSS Doggie Bag containing a dog water bottle, food, shampoo, toy, treats and blinking dog collar light.

Animal Tails

1 pm Winnie’s Nook Storytime

1:30 p.m. BeBop the Therapy Pig

1:45 pm “Twig the Shelter Hog”
Read by Author Marian Thistle

2 p.m. Winnie’s Nook Singalong

2:30 p.m. Featherwing Bird Haven

2:45 p.m. Quire Pages Storytime

3 pm Meadow Browsers Refuge

3:15 p.m. The Hedge Burrow Puppet Show

3:45 pm HPSS Officer Norma

4 p.m. Winnie’s Nook Storytime

Font styles to use
Serif

Colors

Designer to choose colors to be used in the design.

Requirements
Must have
• pig, goat, 2 dogs, kitten, dove, bunny

```html
<!DOCTYPE html>
<html lang="en">
<head>
<meta charset="utf-8">
<title>Birch Hollow Critter MEET</title>
<link rel="stylesheet" href="https://fonts.googleapis.com/css2?family=Montserrat:wght@600;700&family=Lato:ital,wght@0,400;0,700;1,700&family=Dancing+Script:wght@700&display=swap">
<style>
  :root {
    --purple-deep: #2b2466;
    --purple-mid: #4a2a86;
    --purple-glow: #6a2f9c;
    --orange: #f7941d;
    --paper: #eeeeef;
    --paper-light: #f7f7f8;
    --ink: #2a2a2a;
    --rule: #555;
    --logo-grey: #c4c4c6;
    --white: #ffffff;
  }
  html, body { margin: 0; padding: 0; }
  body { width: 986px; height: 1200px; overflow: hidden; background: var(--paper); }
  .flyer { position: relative; width: 986px; height: 1200px; overflow: hidden;
    background: radial-gradient(ellipse at 50% 90%, var(--paper-light), var(--paper) 70%);
    font-family: 'Lato', sans-serif; color: var(--ink); }
  .backdrop { position: absolute; inset: 0; }
  .title { position: absolute; left: 75px; top: 62px; margin: 0; color: var(--white);
    font-family: 'Montserrat', sans-serif; font-weight: 700; line-height: 1; letter-spacing: -1px; }
  .title .place { display: block; font-size: 56px; }
  .title .event { display: block; font-size: 70px; margin-top: 4px; }
  .divider { position: absolute; left: 623px; top: 68px; width: 3px; height: 134px; background: var(--white); }
  .when { position: absolute; left: 643px; top: 72px; color: var(--white);
    font-family: 'Montserrat', sans-serif; font-weight: 700; font-size: 32px; line-height: 42px; }
  .tagline { position: absolute; left: 180px; top: 226px; margin: 0; color: var(--orange);
    font-family: 'Dancing Script', cursive; font-size: 66px; font-weight: 700; white-space: nowrap; }
  .photo { position: absolute; }
  .photo-dove { left: 33px; top: 224px; width: 145px; height: 172px; border-radius: 50% 40% 50% 45%;
    background: radial-gradient(circle at 50% 45%, #ffffff, #d9d9e2 75%); }
  .photo-animals { left: 48px; top: 332px; width: 922px; height: 297px; border-radius: 60px 60px 30px 30px;
    background: linear-gradient(90deg, #f2c2c8 0%, #f2c2c8 14%, #6b6266 18%, #e8e6e6 30%, #c4a078 36%, #c4a078 47%, #9b9592 52%, #b7b0aa 60%, #d8b06e 68%, #d3a55f 84%, #b78a5a 92%, #e5d4bf 100%); }
  .featuring { position: absolute; left: 45px; top: 665px; width: 470px; }
  .section-head { margin: 0; color: var(--orange); font-family: 'Lato', sans-serif; font-weight: 700; font-size: 20px; line-height: 24px; }
  .section-head.caps { font-size: 21px; }
  .partner-list { margin: 4px 0 0; padding: 0; list-style: none; font-size: 15px; line-height: 19px; }
  .partner-list span::before { content: ""; display: inline-block; width: 7px; height: 7px; border-radius: 50%;
    background: var(--orange); margin: 0 5px 2px 0; }
  .rule { position: absolute; left: 40px; width: 306px; height: 1px; background: var(--rule); }
  .block { position: absolute; left: 45px; width: 440px; font-size: 15px; line-height: 19px; }
  .block p { margin: 0; }
  .guest-when { font-style: italic; font-weight: 700; }
  .guest-name { font-weight: 700; }
  .schedule { position: absolute; left: 570px; top: 674px; width: 390px; color: var(--white); }
  .schedule ul { margin: 8px 0 0; padding: 0; list-style: none; font-size: 17px; font-weight: 700; }
  .schedule li { position: absolute; left: 25px; white-space: nowrap; line-height: 21px; }
  .schedule li::before { content: ""; position: absolute; left: -22px; top: 6px; width: 9px; height: 9px;
    border-radius: 50%; background: var(--orange); }
  .sponsors { position: absolute; left: 0; right: 0; top: 1100px; text-align: center; color: var(--logo-grey);
    font-family: 'Lato', sans-serif; font-weight: 700; font-size: 46px; }
</style>
</head>
<body>
<main class="flyer">
  <svg class="backdrop" width="986" height="1200" viewBox="0 0 986 1200" aria-hidden="true">
    <defs>
      <radialGradient id="purpleGlow" cx="0.55" cy="0.55" r="0.7">
        <stop offset="0" stop-color="#6a2f9c"/>
        <stop offset="0.6" stop-color="#4a2a86"/>
        <stop offset="1" stop-color="#2b2466"/>
      </radialGradient>
      <radialGradient id="panelGlow" cx="0.5" cy="0.2" r="0.9">
        <stop offset="0" stop-color="#4a2a86"/>
        <stop offset="1" stop-color="#2b2466"/>
      </radialGradient>
    </defs>
    <path d="M0 0 H986 V432 Q500 520 0 462 Z" fill="url(#purpleGlow)"/>
    <path d="M0 470 Q500 528 986 440" fill="none" stroke="#f7941d" stroke-width="8"/>
    <rect x="543" y="470" width="424" height="580" rx="32" fill="url(#panelGlow)"/>
  </svg>

  <h1 class="title"><span class="place">Birch Hollow</span><span class="event">Critter MEET</span></h1>
  <div class="divider"></div>
  <div class="when">SUNDAY,<br>August 12, 2018<br>1 to 4:30 p.m.</div>
  <p class="tagline">(Fun for Animals In Rescue! )</p>

  <div class="photo photo-dove" role="img" aria-label="White dove in flight"></div>
  <div class="photo photo-animals" role="img" aria-label="Row of animals: pig, goat, bunny, kitten, golden retriever and corgi"></div>

  <section class="featuring">
    <h2 class="section-head">Animal Education &amp; Adoption Event featuring:</h2>
    <ul class="partner-list">
      <li><span>Harbor Pet Shelter &amp; Services Rabbits &amp; Mice</span></li>
      <li><span>Meadow Browsers Goats</span> <span>Kindly Hounds Haven</span></li>
      <li><span>Featherwing Pigeons &amp; Doves</span> <span>Comet Pup Haven</span></li>
      <li><span>Marge’s Feline Haven</span> <span>Marvel Mutt Haven</span></li>
    </ul>
  </section>
  <div class="rule" style="top:776px"></div>

  <section class="block" style="top:782px">
    <p class="guest-when">Special Guest from 1-3 p.m.</p>
    <p class="guest-name">BeBop - SF's 1st Therapy Pig!</p>
    <p>Instagram: @BEBOP_BAYHOG</p>
    <p>Facebook: @BEBOP THE HOG</p>
  </section>
  <div class="rule" style="top:866px"></div>

  <section class="block" style="top:873px">
    <h2 class="section-head caps">ACTIVITIES FOR KIDS</h2>
    <p>Dog &amp; Cat Toy Making with Greta Holloway Canine School Animal Mask Making with Tiny Crafters Face-in-a-Hole Photo Fun with Mark Dorsey Canine School</p>
  </section>
  <div class="rule" style="top:963px"></div>

  <section class="block" style="top:971px">
    <h2 class="section-head caps">HPSS FREE Giveaway!</h2>
    <p>First 75 attending families receive a FREE PSS Doggie Bag containing a dog water bottle, food, shampoo, toy, treats and blinking dog collar light.</p>
  </section>

  <section class="schedule">
    <h2 class="section-head caps">ANIMAL TAILS</h2>
    <ul>
      <li style="top:35px">1 pm Winnie’s Nook Storytime</li>
      <li style="top:63px">1:30 p.m. BeBop the Therapy Pig</li>
      <li style="top:92px">1:45 pm “Twig the Shelter Hog”<br>Read by Author Marian Thistle</li>
      <li style="top:141px">2 p.m. Winnie’s Nook Singalong</li>
      <li style="top:169px">2:30 p.m. Featherwing Bird Haven</li>
      <li style="top:197px">2:45 p.m. Quire Pages Storytime</li>
      <li style="top:225px">3 pm Meadow Browsers Refuge</li>
      <li style="top:255px">3:15 p.m. The Hedge Burrow Puppet Show</li>
      <li style="top:283px">3:45 pm HPSS Officer Norma</li>
      <li style="top:315px">4 p.m. Winnie’s Nook Storytime</li>
    </ul>
  </section>

  <div class="sponsors">sponsoring logos</div>
</main>
</body>
</html>
```